Kveldbrá - Start-up company selling electricity

Hello let me tell you about Kveldbrá.

Kveldbrá is start-up company selling electricity in Iceland. The operations of the company consist of making power usage forecasts for our customers, purchasing the electricity wholesale from the energy producers, and selling the electricity to the consumer. We are focused on tech by using optimization and machine learning to minimize electricity prices to our customers. Our marketing strategy is to portray a tech company mindset and to show dedication to driving down the electricity price on the market.

We need your help to make our website pop. Possible concepts to work with are as follows:

- Iceland the land of ice and fire
- Green energy
- Innovation
- Tech and data science

Link to our website: https://prufa.kveldbra.is/
We are open to ideas.
Thank you!

Target Market(s)

Electricity consumers both homes and companies.

Number of Pages Required

1 page

Font styles to use
Serif
Sans Serif

```html
<!DOCTYPE html>
<html lang="en">
<head>
<meta charset="utf-8">
<title>Kveldbrá – Electricity for homes and companies</title>
<link href="https://fonts.googleapis.com/css2?family=Roboto+Slab:wght@400;500;600;700&family=IBM+Plex+Sans:wght@500;600;700&family=Roboto:wght@300;400;500&display=swap" rel="stylesheet">
<style>
:root{
  --green:#2b7d3b;
  --green-dark:#236b31;
  --text:#222;
  --muted:#8a8a8a;
  --line:#9a9a9a;
  --band:#f6f6f6;
  --white:#fff;
}
*{box-sizing:border-box;margin:0;padding:0}
html,body{width:1200px;height:4195px;overflow:hidden;background:var(--white)}
body{position:relative;font-family:'Roboto',sans-serif;color:var(--text)}
.abs{position:absolute}
.btn{position:absolute;display:flex;align-items:center;justify-content:center;background:var(--green);color:var(--white);font-family:'IBM Plex Sans',sans-serif;font-weight:600;font-size:15px;border-radius:26px;box-shadow:0 3px 8px rgba(0,0,0,.25)}

/* header */
.brand{left:111px;top:22px;display:flex;align-items:center;gap:14px}
.brand-dot{width:58px;height:58px;border-radius:50%;background:var(--green)}
.brand-name{font-family:'Roboto Slab',serif;font-weight:700;font-size:24px;color:var(--green)}
.nav{left:487px;top:48px;display:flex;gap:18px;font-family:'Roboto Slab',serif;font-size:14px;color:#333}
.nav .active{color:var(--green)}

/* hero */
.hero{left:0;top:127px;width:1200px;height:728px;background:linear-gradient(180deg,#6f7f9a 0%,#9a9aa6 30%,#d09a6c 58%,#d88a45 72%,#5a3a22 88%,#111 100%)}
.hero-panel{left:0;top:334px;width:698px;height:291px;background:rgba(60,60,60,.6)}
.hero-title{left:108px;top:350px;font-family:'Roboto Slab',serif;font-weight:700;font-size:66px;color:var(--white);letter-spacing:1px}
.hero-text{left:111px;top:434px;width:570px;font-size:14.5px;line-height:31px;color:#eee}
.dots{left:551px;top:810px;display:flex;gap:14px}
.dots span{width:14px;height:14px;border-radius:50%;border:2px solid #fff}
.dots span:first-child{background:#fff}

/* section headings */
.h2{left:0;width:1200px;text-align:center;color:var(--green);font-size:38px}
.h2.sans{font-family:'IBM Plex Sans',sans-serif;font-weight:600;font-size:34px}
.h2.slab{font-family:'Roboto Slab',serif;font-weight:600;font-size:42px}

/* about */
.about-frame{left:117px;top:1035px;width:471px;height:416px;border:1px solid #ccc;padding:7px}
.photo{width:100%;height:100%}
.about-title{left:601px;top:1046px;width:480px;font-family:'IBM Plex Sans',sans-serif;font-weight:600;font-size:16px;line-height:31px;color:#222}
.about-text{left:601px;width:484px;font-size:14.5px;line-height:31px;color:var(--muted);text-align:justify}

/* prices */
.prices{left:0;top:1558px;width:1200px;height:562px;background:var(--band)}
.card{top:1682px;width:430px;height:377px;background:var(--white);box-shadow:0 0 6px rgba(0,0,0,.12);text-align:center}
.price{margin-top:32px;font-family:'IBM Plex Sans',sans-serif;font-weight:600;font-size:42px;color:var(--green)}
.price small{font-family:'Roboto Slab',serif;font-size:15px;font-weight:500;margin-left:6px}
.plan{margin-top:6px;font-family:'Roboto Slab',serif;font-size:16px;color:#222}
.plan-text{margin:22px auto 0;width:300px;font-size:13px;line-height:31px;color:var(--muted)}
.card .btn{left:78px;top:285px;width:274px;height:50px}

/* future */
.future-title{left:110px;top:2310px;font-family:'Roboto Slab',serif;font-weight:600;font-size:42px;line-height:50px;color:var(--green)}
.future-text{left:111px;top:2432px;width:486px;font-size:15px;line-height:35px;color:var(--muted);text-align:justify}

/* faq */
.faq{width:474px;border:1px solid #555;font-family:'Roboto Slab',serif;font-size:15px;color:#222}
.faq-q{display:flex;justify-content:space-between;align-items:center;height:58px;padding:0 12px 0 10px}
.faq-q b{font-size:20px;font-weight:700}
.faq-a{padding:0 14px 16px;font-family:'Roboto',sans-serif;font-size:11.5px;line-height:26px;color:#666}

/* contact */
.contact{left:0;top:3222px;width:1200px;height:555px;background:radial-gradient(ellipse at 40% 100%,#ffd27a 0%,#f08a2c 25%,#c9561e 55%,#6a2f1c 100%)}
.contact-title{left:627px;top:3252px;font-family:'Roboto Slab',serif;font-weight:600;font-size:31px;color:var(--white)}
.contact-text{left:633px;top:3302px;width:440px;font-family:'Roboto',sans-serif;font-size:14px;line-height:25px;color:#fff}
.field{border-bottom:1px solid rgba(255,255,255,.8);color:#fff;font-size:14px;padding:0 0 10px 6px}
.submit{left:633px;top:3689px;width:411px;height:49px;background:var(--green);color:#fff;display:flex;align-items:center;justify-content:center;font-family:'IBM Plex Sans',sans-serif;font-weight:600;font-size:15px}

/* footer */
.f-head{top:3893px;font-family:'IBM Plex Sans',sans-serif;font-weight:600;font-size:15px;color:#222}
.f-text{font-size:12.5px;line-height:30px;color:var(--muted)}
.f-list{font-size:14.5px;line-height:30px;color:var(--muted)}
.contact-row{left:881px;display:flex;gap:18px;font-size:14.5px;line-height:26px;color:var(--muted)}
.contact-row svg{flex:none;margin-top:5px}
.divider{left:111px;top:4114px;width:978px;height:1px;background:#555}
.copy{left:113px;top:4143px;font-size:13px;color:#666}
.social{left:990px;top:4146px;display:flex;gap:12px}
.social span{width:14px;height:14px;border-radius:50%;background:#666}
</style>
</head>
<body>

<header>
  <div class="abs brand"><span class="brand-dot"></span><span class="brand-name">KVELDBRÁ</span></div>
  <nav class="abs nav">
    <span class="active">Home</span><span>About us</span><span>Terms of business</span><span>Question &amp; Answer</span><span>About Kveldbrá</span><span>Contact</span>
  </nav>
</header>

<section>
  <div class="abs hero" role="img" aria-label="Power transmission towers against a sunset sky"></div>
  <div class="abs hero-panel"></div>
  <h1 class="abs hero-title">KVELDBRÁ</h1>
  <p class="abs hero-text">Kveldbrá uses automation and artificial intelligence to achieve lower prices in the electricity market. Our goal is to minimize the cost of energy sales, promote energy balance and offer good service.</p>
  <div class="btn" style="left:111px;top:545px;width:154px;height:49px">GET STARTED</div>
  <div class="abs dots"><span></span><span></span><span></span><span></span></div>
</section>

<section>
  <h2 class="abs h2 sans" style="top:945px">ABOUT KVELDBRÁ</h2>
  <div class="abs about-frame"><div class="photo" role="img" aria-label="Telecom towers on a hill at sunset" style="background:linear-gradient(180deg,#5a6a86 0%,#9a8a80 35%,#e59a48 55%,#4a5a2c 75%,#2c3a1c 100%)"></div></div>
  <h3 class="abs about-title">WHAT IS KVELDBRÁ'S UNIQUE POSITION IN THE ELECTRICITY SALES MARKET?</h3>
  <p class="abs about-text" style="top:1125px">Kveldbrá uses automation and artificial intelligence to achieve lower prices in the electricity market. Our goal is to minimize the cost of energy sales, promote energy balance and offer good service</p>
  <p class="abs about-text" style="top:1236px">Kveldbrá's goal is to offer its customers the most favorable electricity prices in Iceland. Electricity is part of the monthly costs of households and companies, and by doing business with Kveldbrá, savings can be achieved and operating costs reduced.</p>
  <div class="btn" style="left:601px;top:1384px;width:153px;height:50px">READ MORE</div>
</section>

<section>
  <div class="abs prices"></div>
  <h2 class="abs h2 slab" style="top:1604px">PRICE LIST</h2>
  <div class="abs card" style="left:160px">
    <div class="price">6.95<small>ISK / KWH</small></div>
    <div class="plan">Electric Acceleration</div>
    <p class="plan-text">Sed ut perspiciatis unde omnis iste natus error sit voluptatem accusantium doloremque laudantium, totam rem aperiam, eaque ipsa quae ab illo inventore veritatis et quasi</p>
    <div class="btn">MAKE A PRICE COMPARISON</div>
  </div>
  <div class="abs card" style="left:610px">
    <div class="price">6.22<small>ISK / KWH</small></div>
    <div class="plan">Electric Acceleration</div>
    <p class="plan-text">Sed ut perspiciatis unde omnis iste natus error sit voluptatem accusantium doloremque laudantium, totam rem aperiam, eaque ipsa quae ab illo inventore veritatis et quasi</p>
    <div class="btn">MAKE A PRICE COMPARISON</div>
  </div>
</section>

<section>
  <h2 class="abs future-title">THE FUTURE IS<br>EXCITING</h2>
  <p class="abs future-text">Let's make the electricity system smarter together. Kveldbrá uses artificial intelligence, data science and automation to minimize costs and promote eccentricity</p>
  <div class="abs" role="img" aria-label="City at dusk with glowing network connections" style="left:625px;top:2217px;width:461px;height:420px;background:radial-gradient(ellipse at 55% 60%,#2f7fd0 0%,#1b3f78 45%,#0d1a33 100%)"></div>
</section>

<section>
  <h2 class="abs h2 slab" style="top:2730px">QUESTION &amp; ANSWER</h2>
  <div class="abs faq" style="left:117px;top:2824px"><div class="faq-q">Can anyone buy electricity from Kveldbrá?<b>+</b></div></div>
  <div class="abs faq" style="left:117px;top:2893px"><div class="faq-q">How do I buy electricity from Kveldbrá?<b>+</b></div></div>
  <div class="abs faq" style="left:117px;top:2961px"><div class="faq-q">Does it cost to switch to Kveldbrá?<b>+</b></div></div>
  <div class="abs faq" style="left:607px;top:2824px"><div class="faq-q">What happens after I sign up for a business?<b>+</b></div></div>
  <div class="abs faq" style="left:607px;top:2893px"><div class="faq-q">The future with Kveldbrá?<b>+</b></div></div>
  <div class="abs faq" style="left:607px;top:2961px;height:158px"><div class="faq-q">How do I quit trading?<b>-</b></div>
    <p class="faq-a">It is not a problem to cease trading with Kveldbrá, according to Kveldbrá's general business terms, the customer can terminate the contract with 3 weeks notice and the termination will take effect at the end of next month.</p></div>
</section>

<section>
  <div class="abs contact" role="img" aria-label="Power transmission towers silhouetted against an orange sunset"></div>
  <h2 class="abs contact-title">GET IN TOUCH</h2>
  <p class="abs contact-text">Lorem ipsum dolor sit amet, consectetur adipiscing elit, sed do eiusmod tempor incididunt ut labore et</p>
  <div class="abs field" style="left:633px;top:3394px;width:186px">First Name</div>
  <div class="abs field" style="left:852px;top:3394px;width:192px">Last Name</div>
  <div class="abs field" style="left:633px;top:3471px;width:411px">Email Address</div>
  <div class="abs field" style="left:633px;top:3548px;width:411px">Phone Number</div>
  <div class="abs field" style="left:633px;top:3622px;width:411px">Message</div>
  <div class="abs submit">SUBMIT</div>
</section>

<footer>
  <h4 class="abs f-head" style="left:111px">ABOUT US</h4>
  <p class="abs f-text" style="left:111px;top:3926px;width:260px">Kveldbrá uses automation and artificial intelligence to achieve lower prices in the electricity market. Our goal is to minimize the cost of energy sales, promote energy balance and offer good service</p>
  <h4 class="abs f-head" style="left:428px">KVELDBRÁ EHF</h4>
  <p class="abs f-list" style="left:428px;top:3926px">ID number: 610521-0390<br>VAT number: 204871</p>
  <h4 class="abs f-head" style="left:677px">QUICK LINKS</h4>
  <p class="abs f-list" style="left:677px;top:3926px">Home<br>Terms of business<br>Question &amp; Answer<br>About Kveldbrá</p>
  <h4 class="abs f-head" style="left:881px">CONTACT US</h4>
  <div class="abs contact-row" style="top:3930px">
    <svg width="16" height="16" viewBox="0 0 24 24" fill="none" stroke="#555" stroke-width="2"><path d="M5 3h4l2 5-3 2a12 12 0 0 0 6 6l2-3 5 2v4a2 2 0 0 1-2 2A18 18 0 0 1 3 5a2 2 0 0 1 2-2z"/></svg>
    <span>555-0142</span></div>
  <div class="abs contact-row" style="top:3972px">
    <svg width="14" height="18" viewBox="0 0 24 30"><path d="M12 0a10 10 0 0 0-10 10c0 8 10 20 10 20s10-12 10-20A10 10 0 0 0 12 0zm0 14a4 4 0 1 1 0-8 4 4 0 0 1 0 8z" fill="#222"/></svg>
    <span>Lindargata 42<br>101 Reykjavík</span></div>
  <div class="abs contact-row" style="top:4046px">
    <svg width="16" height="14" viewBox="0 0 24 18" fill="none" stroke="#555" stroke-width="2"><rect x="1" y="1" width="22" height="16"/><path d="M1 1l11 9 11-9"/></svg>
    <span>hallo@kveldbra.is</span></div>
  <div class="abs divider"></div>
  <p class="abs copy">© 2021 All Rights Reserved</p>
  <div class="abs social"><span></span><span></span><span></span><span></span></div>
</footer>

</body>
</html>
```